Wedding and event Photography company.

We need a business card design for a photography company based in Singapore named LumaVek. Our core service offering is wedding photojournalism. We would like to see minimalistic designs that use the colour white. The final design should communicate a sense of ease and reliability.

The attached are a couple of visual reference which i found over the web, i hope it will helps.

Project Brief Update (14th July 2014):
- Please refrain from using any images from the website for the design. The laws and regulations over here does not allow me to distribute my client's images. Thanks!

Target Market(s)

Young and middle aged adults aged 24 - 38. With money to spend =D

Industry/Entity Type

Business

Contact Information for Business Card

Name: Dax Pell
Designation: Head Photographer
Mobile: +65 84126079
Email: tan@lumavek.example
Website: www.lumavek.example

Font styles to use
Other font styles liked:
• Baskerville URW

Colors

Designer to choose colors to be used in the design.

Requirements
Must have
• Must include:
• - The brand LumaVek
• - The logo attached
• - Please help to place the brand LumaVek with the logo according to your preferences.
• - Services
• - Wedding Photography
• - Portraiture
• - Photojournalism
Nice to have
• Looking forward to an elegant and simple design. Please see attached examples!
• Please use Serif Fonts
Should not have
• Please refrain from using dark tones for the majority of the design.
• Please refrain from letterpress and embossing.

```html
<!DOCTYPE html>
<html lang="en">
<head>
<meta charset="utf-8">
<title>LumaVek Business Card</title>
<link rel="stylesheet" href="https://fonts.googleapis.com/css2?family=Libre+Baskerville:ital,wght@0,400;0,700;1,400&display=swap">
<style>
  :root {
    --page-bg: #ffffff;
    --card-bg: #ffffff;
    --pattern-grey: #efefef;
    --card-edge: #d2d2d2;
    --text-grey: #5a5a5a;
    --brand-navy: #1f3a63;
  }
  * { margin: 0; padding: 0; box-sizing: border-box; }
  html, body {
    width: 947px;
    height: 1200px;
    overflow: hidden;
    background: var(--page-bg);
  }
  .canvas {
    position: relative;
    width: 947px;
    height: 1200px;
  }
  .card {
    position: absolute;
    top: 476px;
    width: 386px;
    height: 248px;
    background: var(--card-bg);
    border: 1px solid var(--card-edge);
    box-shadow: 2px 3px 4px rgba(0, 0, 0, 0.18);
    overflow: hidden;
    font-family: "Libre Baskerville", "Baskerville", Georgia, serif;
    color: var(--text-grey);
  }
  .card--front { left: 54px; }
  .card--back { left: 506px; }
  .card__pattern {
    position: absolute;
    inset: 0;
    background:
      linear-gradient(135deg, var(--pattern-grey) 0%, #f7f7f7 45%, var(--pattern-grey) 100%);
  }
  .brand {
    position: absolute;
    left: 145px;
    top: 84px;
    transform: translateX(-50%);
    display: flex;
    flex-direction: column;
    align-items: center;
    gap: 12px;
  }
  .brand__name {
    font-size: 25px;
    font-weight: 400;
    letter-spacing: -0.5px;
    color: var(--text-grey);
    white-space: nowrap;
  }
  .brand__mark {
    width: 14px;
    height: 14px;
    background: var(--brand-navy);
  }
  .contact {
    position: absolute;
    left: 145px;
    top: 74px;
    transform: translateX(-50%);
    text-align: center;
    white-space: nowrap;
  }
  .contact__name {
    font-size: 14px;
    font-weight: 700;
    letter-spacing: 0.5px;
    text-transform: uppercase;
    line-height: 18px;
  }
  .contact__role {
    font-size: 12px;
    font-style: italic;
    line-height: 18px;
    margin-bottom: 14px;
  }
  .contact__line {
    font-size: 12.5px;
    line-height: 17.5px;
    letter-spacing: 0.3px;
  }
</style>
</head>
<body>
  <main class="canvas">
    <section class="card card--front">
      <div class="card__pattern" role="img" aria-label="Soft grey aperture blade pattern"></div>
      <div class="brand">
        <span class="brand__name">LumaVek</span>
        <span class="brand__mark"></span>
      </div>
    </section>

    <section class="card card--back">
      <div class="card__pattern" role="img" aria-label="Soft grey aperture blade pattern"></div>
      <div class="contact">
        <p class="contact__name">Dax Pell</p>
        <p class="contact__role">Head Photographer</p>
        <p class="contact__line">+65 84126079</p>
        <p class="contact__line">tan@lumavek.example</p>
        <p class="contact__line">www.lumavek.example</p>
      </div>
    </section>
  </main>
</body>
</html>
```